Carton Box Packaging For Motorcycle Electric Regulator - Brevora Brand

Packaging Dimensions: 7cm (H) x 6cm (W) x 2.5cm (D)
We would like to design a genuine Carton box Packaging for motorcycle electric regulator.
This is a sensitive part of the motorcycle, so we need the packaging to reflect elegant impression.
Brevora, is one of the leading companies for manufacturing Motorcycles, located in Egypt. Our company is offering high-quality products, the best in the local market, with very competitive prices.
We have a limited time to get this project done, So we Highly appreciate receiving your designs ASAP.
Target Market(s)
Motorcycle Parts Buyers
Font styles to use
Colors
Designer to choose colors to be used in the design.
Look and feel
Each slider illustrates characteristics of the customer's brand and the style your logo design should communicate.

```html
<!DOCTYPE html>
<html lang="en">
<head>
<meta charset="utf-8">
<title>Brevora – Motorcycle Regulator Carton Dieline</title>
<link rel="stylesheet" href="https://fonts.googleapis.com/css2?family=Audiowide&display=swap">
<style>
  :root {
    --page: #ffffff;
    --carton: #231f20;
    --flap-edge: #302c2d;
    --fold: #38332f;
    --accent-red: #c1272d;
    --panel-light: #f7f7f7;
    --panel-mid: #d9d9d9;
    --mark-grey: #5a5a5a;
  }
  html, body {
    margin: 0;
    padding: 0;
    width: 1200px;
    height: 1200px;
    overflow: hidden;
    background: var(--page);
  }
  .dieline {
    display: block;
    width: 1200px;
    height: 1200px;
  }
  .carton-shapes { filter: drop-shadow(0 4px 14px rgba(0,0,0,0.35)); }
  .carton { fill: var(--carton); }
  .flap-edge { fill: var(--flap-edge); }
  .fold-line { stroke: var(--fold); stroke-width: 1; fill: none; }
  .diagonal-stripe { fill: var(--carton); }
  .brand-name {
    font-family: "Audiowide", sans-serif;
    font-size: 12px;
    fill: var(--mark-grey);
  }
  .brand-dot { fill: var(--mark-grey); }
  .product-title {
    font-family: "Audiowide", sans-serif;
    font-size: 22px;
    font-style: italic;
    fill: var(--accent-red);
  }
</style>
</head>
<body>
<svg class="dieline" viewBox="0 0 900 900" xmlns="http://www.w3.org/2000/svg">
  <defs>
    <linearGradient id="panel-texture" x1="0" y1="0" x2="1" y2="1">
      <stop offset="0" stop-color="#cfcfcf"/>
      <stop offset="0.45" stop-color="#ececec"/>
      <stop offset="1" stop-color="#ffffff"/>
    </linearGradient>
    <linearGradient id="regulator-tone" x1="0" y1="0" x2="1" y2="1">
      <stop offset="0" stop-color="#ffffff"/>
      <stop offset="0.35" stop-color="#3a3a3a"/>
      <stop offset="0.75" stop-color="#1c1c1c"/>
      <stop offset="1" stop-color="#f2f2f2"/>
    </linearGradient>
  </defs>

  <g class="carton-shapes">
    <!-- front panel with top closure -->
    <path class="flap-edge" d="M47,621 V145 Q47,131 61,131 H324 Q338,131 338,145 V621 Z"/>
    <rect class="carton" x="47" y="160" width="291" height="461"/>

    <!-- left side panel and dust flaps -->
    <polygon class="carton" points="345,160 452,160 452,262 460,283 338,283 345,262"/>
    <rect class="carton" x="338" y="283" width="122" height="338"/>
    <polygon class="carton" points="338,621 460,621 452,642 452,741 345,741 345,642"/>

    <!-- back panel with bottom closure -->
    <rect class="carton" x="460" y="283" width="290" height="338"/>
    <path class="flap-edge" d="M460,621 V756 Q460,770 474,770 H736 Q750,770 750,756 V621 Z"/>
    <rect class="carton" x="460" y="621" width="290" height="120"/>

    <!-- right side panel and dust flaps -->
    <polygon class="carton" points="757,160 860,160 860,262 872,283 750,283 757,262"/>
    <rect class="carton" x="750" y="283" width="122" height="338"/>
    <polygon class="carton" points="750,621 872,621 860,642 860,741 757,741 757,642"/>
  </g>

  <!-- fold lines -->
  <g class="fold-lines">
    <line class="fold-line" x1="338" y1="160" x2="338" y2="621"/>
    <line class="fold-line" x1="460" y1="283" x2="460" y2="621"/>
    <line class="fold-line" x1="750" y1="283" x2="750" y2="621"/>
    <line class="fold-line" x1="338" y1="283" x2="460" y2="283"/>
    <line class="fold-line" x1="750" y1="283" x2="872" y2="283"/>
    <line class="fold-line" x1="47" y1="621" x2="872" y2="621"/>
  </g>

  <!-- front panel artwork -->
  <g class="front-panel">
    <rect x="47" y="283" width="291" height="209" fill="url(#panel-texture)" role="img" aria-label="Light grey geometric background texture"/>
    <polygon class="diagonal-stripe" points="188,283 245,283 192,492 125,492"/>
    <circle class="brand-dot" cx="104" cy="330" r="20"/>
    <text class="brand-name" x="104" y="370" text-anchor="middle">Brevora</text>
    <rect x="215" y="372" width="118" height="115" rx="6" fill="url(#regulator-tone)" role="img" aria-label="Photo of the motorcycle voltage regulator with its wiring and connector"/>
    <text class="product-title" x="193" y="556" text-anchor="middle" textLength="262" lengthAdjust="spacingAndGlyphs">motorcycle regulator</text>
  </g>

  <!-- back panel artwork -->
  <g class="back-panel">
    <rect x="460" y="283" width="290" height="209" fill="url(#panel-texture)" role="img" aria-label="Light grey geometric background texture"/>
    <polygon class="diagonal-stripe" points="600,283 660,283 605,492 540,492"/>
    <circle class="brand-dot" cx="517" cy="330" r="20"/>
    <text class="brand-name" x="517" y="370" text-anchor="middle">Brevora</text>
    <rect x="628" y="372" width="117" height="115" rx="6" fill="url(#regulator-tone)" role="img" aria-label="Photo of the motorcycle voltage regulator with its wiring and connector"/>
    <text class="product-title" x="607" y="556" text-anchor="middle" textLength="262" lengthAdjust="spacingAndGlyphs">motorcycle regulator</text>
  </g>
</svg>
</body>
</html>
```